Letterhead Design Needed for Real Estate Office

We are a boutique real estate agency focused on property management. We need a letter head which is professional looking and include the following information:

Logo
ABN Number
Address
Postal Address
Phone
Fax
Mobile
Email
Website

Please note that the PLBVKT logo can not be changed and must be positioned at the bottom right corner.

Please find attached the existing letterhead design for all the required elements.

Target Market(s)

Letterhead mostly used for service of notices, business letters, clients communication

Industry/Entity Type

Boutique

Colors

Designer to choose colors to be used in the design.

Requirements
Must have
• Logo

```html
<!DOCTYPE html>
<html lang="en">
<head>
<meta charset="utf-8">
<title>Meridian Partners Real Estate – Letterhead</title>
<link rel="stylesheet" href="https://fonts.googleapis.com/css2?family=Source+Sans+3:wght@400;600;700&display=swap">
<style>
  :root {
    --paper: #ffffff;
    --brand-blue: #2a8fd8;
    --brand-navy: #1d2b46;
    --brand-grey: #6d7787;
    --sketch-light: #eef4fa;
    --sketch-mid: #d6e6f5;
    --sketch-accent: #9cc7ec;
  }
  * { box-sizing: border-box; margin: 0; padding: 0; }
  html, body {
    width: 855px; height: 1200px; overflow: hidden;
    background: var(--paper);
    font-family: "Source Sans 3", "Myriad Pro", Arial, sans-serif;
  }
  .letterhead {
    position: relative; width: 855px; height: 1200px;
    background: var(--paper); overflow: hidden;
  }
  .harbour-sketch-top {
    position: absolute; left: 420px; top: 0; width: 435px; height: 135px;
    background: linear-gradient(200deg, var(--sketch-mid) 0%, var(--sketch-light) 55%, rgba(255,255,255,0) 100%);
  }
  .brand {
    position: absolute; left: 63px; top: 62px;
    display: flex; align-items: center; gap: 14px;
  }
  .brand-mark {
    width: 58px; height: 58px; background: var(--brand-blue);
  }
  .brand-name {
    color: var(--brand-navy); font-weight: 700; font-size: 30px;
    line-height: 1; letter-spacing: 1px;
  }
  .brand-name span { display: block; }
  .contact {
    position: absolute; left: 0; right: 0; top: 136px;
    text-align: center; color: var(--brand-blue);
    font-size: 13px; font-weight: 600; line-height: 24px; letter-spacing: 0.1px;
  }
  .skyline-sketch-bottom {
    position: absolute; left: 0; bottom: 0; width: 855px; height: 295px;
    background: linear-gradient(180deg, rgba(255,255,255,0) 0%, var(--sketch-light) 30%, var(--sketch-mid) 80%, var(--sketch-accent) 100%);
  }
  .membership {
    position: absolute; right: 42px; bottom: 30px;
    display: flex; align-items: center; gap: 8px;
    background: var(--paper); padding: 8px 12px;
  }
  .membership-square { width: 26px; height: 26px; background: var(--brand-blue); }
  .membership-name {
    color: var(--brand-blue); font-weight: 700; font-size: 32px; line-height: 1;
  }
</style>
</head>
<body>
<main class="letterhead">
  <div class="harbour-sketch-top" role="img" aria-label="Faint line sketch of the harbour opera house sails"></div>

  <header>
    <div class="brand">
      <div class="brand-mark"></div>
      <div class="brand-name"><span>MERIDIAN</span><span>PARTNERS</span></div>
    </div>
    <p class="contact">
      ABN&nbsp; 48 203 615 972 | Shop 12B 310-322 Harbour Street Lindfield NSW 2070 AUSTRALIA | PO BOX 415 Lindfield NSW 2070<br>
      m&nbsp; 0400 123 456 &nbsp;| p&nbsp; 9000 1234 &nbsp;| f&nbsp; 9000 5678 &nbsp;| e&nbsp; hello@mpre.cc &nbsp;| w&nbsp; http://mpre.cc
    </p>
  </header>

  <footer>
    <div class="skyline-sketch-bottom" role="img" aria-label="Line sketch of the city skyline and opera house with blue window accents"></div>
    <div class="membership">
      <div class="membership-square"></div>
      <span class="membership-name">PLBVKT</span>
    </div>
  </footer>
</main>
</body>
</html>
```